Need a design package for hair towels wrap

We need package design for hair towel wrap ( 3 pack) brand name is The Quorin. We are looking for simple, contemporary and unique design, color palette 2-3 colors. Paper Box size is 9*8*3 inches with PVC window.Actual picture of the product won't be on the package.Attached Brand Logo and description for the package. Barcode needed to be included on the design package.It will be provided later. Attached sample of the box from manufacturer, and instruction for towel wrap which idea I like, if you could make something similar to it, would be great.

Target Market(s)

Zelvora

Industry/Entity Type

Hair

Colors
848484
f5f5f5
faa54b
333333

Requirements
Must have
• Clean, contemporary design.

```html
<!DOCTYPE html>
<html lang="en">
<head>
<meta charset="utf-8">
<title>The Quorin – Microfiber Hair Towel Wrap Box</title>
<link rel="stylesheet" href="https://fonts.googleapis.com/css2?family=Poppins:wght@500;600;700;800&display=swap">
<style>
  :root {
    --backdrop: #e6ddd1;
    --box-face: #f4f0e7;
    --window-light: #efe7de;
    --window-mid: #ddd0c2;
    --ink: #111111;
    --paper: #ffffff;
    --gold: #c9932e;
  }
  * { margin: 0; padding: 0; box-sizing: border-box; }
  html, body { width: 1200px; height: 1067px; overflow: hidden; }
  body {
    background: var(--backdrop);
    font-family: "Poppins", Arial, sans-serif;
    position: relative;
  }
  .box-front {
    position: absolute;
    left: 100px; top: 170px;
    width: 1000px; height: 727px;
    background: var(--box-face);
  }
  .pvc-window {
    position: absolute;
    left: 50px; top: 39px;
    width: 434px; height: 623px;
    border-radius: 30px;
    background: linear-gradient(160deg, var(--window-light) 0%, var(--window-mid) 55%, var(--window-light) 100%);
    box-shadow: inset 0 0 0 2px rgba(255,255,255,0.6);
  }
  .brand-frame {
    position: absolute;
    left: 505px; top: 87px;
    width: 348px; height: 202px;
    border: 4px solid var(--ink);
    display: flex; flex-direction: column;
    align-items: center; justify-content: center;
    gap: 22px;
  }
  .brand-mark {
    width: 44px; height: 44px;
    background: var(--gold);
  }
  .brand-name {
    font-weight: 700;
    font-size: 38px;
    letter-spacing: 1px;
    color: var(--ink);
    line-height: 1;
  }
  .product-band {
    position: absolute;
    left: 505px; top: 336px;
    width: 495px; height: 70px;
    background: var(--ink);
    color: var(--paper);
    padding-left: 26px;
    display: flex; flex-direction: column; justify-content: center;
    line-height: 1.15;
  }
  .product-type { font-weight: 700; font-size: 17px; }
  .product-count { font-weight: 800; font-size: 25px; }
  .benefit-list {
    position: absolute;
    left: 701px; top: 447px;
    list-style: none;
    font-weight: 700;
    font-size: 11.5px;
    color: var(--ink);
    line-height: 19px;
  }
  .benefit-list li::before {
    content: "";
    display: inline-block;
    width: 5px; height: 5px;
    border-radius: 50%;
    background: var(--ink);
    margin-right: 9px;
    vertical-align: middle;
  }
</style>
</head>
<body>
  <main class="box-front">
    <div class="pvc-window" role="img" aria-label="Clear PVC window showing the folded beige microfiber hair towels inside"></div>

    <div class="brand-frame">
      <div class="brand-mark"></div>
      <div class="brand-name">THE QUORIN</div>
    </div>

    <div class="product-band">
      <span class="product-type">Microfiber Hair Towel Wrap</span>
      <span class="product-count">Set of 3 Hair Towels</span>
    </div>

    <ul class="benefit-list">
      <li>The softest</li>
      <li>ultra-absorbent</li>
      <li>light &amp; fastest</li>
      <li>Towel for your beautiful hair</li>
    </ul>
  </main>
</body>
</html>
```